brightquill 2 page brochure

We need some design input for a corporate brochure.
PDF of the content to be designed around is as attached - and also png images used in the mockup.
This will be used for corporate marketing to senior execs in big companies - so needs to look professional and fun at the same time.
Feel free to make whatever design changes you like and we will give good feedback.
Just made this a guaranteed payment - looking forward to receiving lots of great designs!
To appeal to corporate marketing executives
Marketing

```html
<!DOCTYPE html>
<html lang="en">
<head>
<meta charset="utf-8">
<title>brightquill brochure</title>
<link rel="stylesheet" href="https://fonts.googleapis.com/css2?family=Varela+Round&family=Oswald:wght@300;400&display=swap">
<style>
  :root {
    --red-bright: #e00a0a;
    --red-mid: #c20606;
    --red-deep: #8e0202;
    --ring: #6d0808;
    --white: #ffffff;
    --brand-red: #c0192b;
    --navy: #0f2d52;
    --navy-deep: #0a1f3b;
    --band-edge: #3c76b4;
    --device-dark: #1c1c22;
    --device-mid: #4a4f5c;
  }
  html, body {
    margin: 0;
    padding: 0;
    width: 848px;
    height: 1200px;
    overflow: hidden;
  }
  .page {
    position: relative;
    width: 848px;
    height: 1200px;
    background: radial-gradient(ellipse 70% 55% at 50% 52%, var(--red-bright) 0%, var(--red-mid) 55%, var(--red-deep) 100%);
    overflow: hidden;
    font-family: "Oswald", sans-serif;
  }
  .emblem-shadow {
    position: absolute;
    left: 170px;
    top: 630px;
    width: 520px;
    height: 40px;
    border-radius: 50%;
    background: radial-gradient(ellipse at center, rgba(60,0,0,0.45) 0%, rgba(60,0,0,0) 70%);
  }
  .emblem {
    position: absolute;
    left: 157px;
    top: 105px;
    width: 550px;
    height: 550px;
    border-radius: 50%;
    background: var(--ring);
    display: flex;
    align-items: center;
    justify-content: center;
  }
  .emblem-face {
    width: 490px;
    height: 490px;
    border-radius: 50%;
    background: var(--white);
    display: flex;
    align-items: center;
    justify-content: center;
  }
  .emblem-name {
    font-family: "Varela Round", sans-serif;
    font-size: 44px;
    color: var(--brand-red);
  }
  .wordmark {
    position: absolute;
    left: 0;
    right: 0;
    top: 690px;
    margin: 0;
    text-align: center;
    font-family: "Varela Round", sans-serif;
    font-weight: 400;
    font-size: 122px;
    letter-spacing: 1px;
    color: var(--white);
  }
  .intro-band {
    position: absolute;
    left: 0;
    top: 932px;
    width: 848px;
    height: 132px;
    background: linear-gradient(to bottom, var(--navy) 0%, var(--navy-deep) 100%);
    border-top: 3px solid var(--band-edge);
    border-bottom: 3px solid var(--band-edge);
    box-sizing: border-box;
    display: flex;
    align-items: center;
    justify-content: center;
  }
  .intro-text {
    margin: 0;
    width: 600px;
    text-align: center;
    color: var(--white);
    font-weight: 300;
    font-size: 19.5px;
    line-height: 29px;
  }
  .device-row {
    position: absolute;
    left: 272px;
    top: 1068px;
    width: 326px;
    height: 74px;
    border-radius: 6px 6px 14px 14px;
    background: linear-gradient(to bottom, var(--device-mid) 0%, var(--device-dark) 100%);
  }
</style>
</head>
<body>
  <main class="page">
    <div class="emblem-shadow"></div>
    <div class="emblem">
      <div class="emblem-face">
        <span class="emblem-name">brightquill</span>
      </div>
    </div>

    <h1 class="wordmark">brightquill</h1>

    <section class="intro-band">
      <p class="intro-text">Brightquill helps organisations increase the value of their brands and media rights through inplay mobile games based on live sports events, tv talent contests and other popular events.</p>
    </section>

    <div class="device-row" role="img" aria-label="Row of smartphones fanned out, each showing a sponsored mobile game screen"></div>
  </main>
</body>
</html>
```